Yacht, Boats, Watersports company needs a redesign of business card

Hello Designers!
We are a Boat dealership company that sells fun in the water, we sell boats, Yachts, Kayaks and also yacht WaterSport toys. We are looking to redesign our business cards in to something a little bit more sophisticated. in a way that we can make better use of our company colors. I'm attaching a zipped file containing the company 3 sets of company logo which one is an horizontal another one is a vertical and also a chromed 3d logo. Also is included two set of business cards that we use and also some designs that i think it's interesting. We use PMS 2026c Orange and PMS 7687C Blue. I would like to see at least two different options with the orange as accent and also using blue as an accent color. It's really important for the business cards to have a font option and size that is legible to most people. Our current website is wwww.corvellamarine.com. Please visit if you want to have a better feeling of the Boat dealership
You can send Single sided or double side options. We are now using single sided but we may be open for a double side option if we really like the design.
Target Market(s)
Marine, boat sales, yacht sales, water toys sales/
Contact Information for Business Card
Name: Dale Pritchett
Address: 718 West Halden Lane,
Dania Beach, FL 33019
Phone: 954-382-7146
Fax: 954:382-7139
Cell: 954-451-8320
Email: 212@corvellamarine.com
Website: corvellamarine.com
Requirements
Must have
- the current information of the business card provided.
logo
use the PMS Colors
Nice to have
- a touch of elegance and sophistication but simple
Should not have
- should not have any typography that is hard to read, the card should be simple but yet sophisticated.

```html
<!DOCTYPE html>
<html lang="en">
<head>
<meta charset="utf-8">
<title>Corvella Marine – Business Card</title>
<link href="https://fonts.googleapis.com/css2?family=Poppins:wght@400;600&display=swap" rel="stylesheet">
<style>
  :root{
    --bg:#d9dadc;
    --blue:#1360b0;
    --orange:#ea7a1c;
    --white:#ffffff;
  }
  *{margin:0;padding:0;box-sizing:border-box}
  html,body{width:1200px;height:800px;overflow:hidden}
  body{background:var(--bg);font-family:"Poppins",sans-serif;position:relative}
  .card{position:absolute;background:var(--blue);border-radius:22px;border-bottom:3px solid var(--orange);border-right:3px solid var(--orange)}
  .card-contact{left:150px;top:110px;width:330px;height:580px}
  .card-brand{left:540px;top:240px;width:580px;height:330px}

  .mark-ring{position:absolute;left:45px;top:40px;width:240px;height:240px;border-radius:50%;border:18px solid var(--orange);display:flex;align-items:center;justify-content:center}
  .mark-name{color:var(--white);font-weight:600;font-size:26px;line-height:1.15;text-align:center;letter-spacing:1px}

  .contact{position:absolute;left:34px;bottom:36px;color:var(--white);font-size:15px;line-height:1.5}
  .contact-name{color:var(--orange);font-weight:600;font-size:23px;letter-spacing:1px;text-transform:uppercase;margin-bottom:6px}
  .contact-address{margin-bottom:10px}
  .contact-row{display:flex;align-items:center;gap:10px}
  .contact-row svg{width:14px;height:14px;flex:none;fill:var(--orange)}

  .brand{position:absolute;left:0;right:0;top:95px;display:flex;flex-direction:column;align-items:center;gap:18px}
  .brand-dot{width:78px;height:78px;border-radius:50%;border:9px solid var(--orange)}
  .brand-name{color:var(--white);font-weight:600;font-size:40px;letter-spacing:3px;text-transform:uppercase}
</style>
</head>
<body>
  <section class="card card-contact">
    <div class="mark-ring"><span class="mark-name">Corvella<br>Marine</span></div>
    <div class="contact">
      <p class="contact-name">Dale Pritchett</p>
      <p class="contact-address">718 West Halden Lane,<br>Dania Beach, FL 33019</p>
      <p class="contact-row"><svg viewBox="0 0 16 16" aria-hidden="true"><path d="M3 1l3 3-2 2c1 2 3 4 5 5l2-2 3 3-2 3C6 15 1 10 0 4z"/></svg>954-382-7146</p>
      <p class="contact-row"><svg viewBox="0 0 16 16" aria-hidden="true"><path d="M4 1h7v4H4zM1 6h14v7h-3v2H4v-2H1zM5 10v4h6v-4z"/></svg>954-451-8320</p>
      <p class="contact-row"><svg viewBox="0 0 16 16" aria-hidden="true"><path d="M4 0h8a1 1 0 011 1v14a1 1 0 01-1 1H4a1 1 0 01-1-1V1a1 1 0 011-1zm1 2v10h6V2z"/></svg>954:382-7139</p>
      <p class="contact-row"><svg viewBox="0 0 16 16" aria-hidden="true"><path d="M0 3h16v10H0zm2 2v1l6 4 6-4V5L8 9z"/></svg>212@corvellamarine.com</p>
      <p class="contact-row"><svg viewBox="0 0 16 16" aria-hidden="true"><path d="M8 0a8 8 0 100 16A8 8 0 008 0zm0 2c1 1 2 3 2 6s-1 5-2 6c-1-1-2-3-2-6s1-5 2-6z"/></svg>corvellamarine.com</p>
    </div>
  </section>

  <section class="card card-brand">
    <div class="brand">
      <span class="brand-dot"></span>
      <span class="brand-name">Corvella Marine</span>
    </div>
  </section>
</body>
</html>
```